Illustration Style Book Cover for Business Book

I have written a book called "The Corner Shop Keeper's Handbook". The title should be self-explanatory. It's a how-to for the owner or manager of a small business on a variety of subjects like makreting, operations, finance, managing people, etc.
I have no pre-defined notions about what i want this to look like and I would like the designer to take full creative license. The "owners manual" concept should come through in the design.

Target Market(s)

Small Business Owners and Operators

Industry/Entity Type

All - Small business

Font styles to use
Sans Serif

Colors

Designer to choose colors to be used in the design.

Requirements
Nice to have
• Should look like an “owners manual"
Should not have
• Photos

```html
<!DOCTYPE html>
<html lang="en">
<head>
<meta charset="utf-8">
<title>The Corner Shop Keeper's Handbook — Cover</title>
<link rel="stylesheet" href="https://fonts.googleapis.com/css2?family=Montserrat:wght@300;400;800&display=swap">
<style>
  :root {
    --page-bg: #d3d0d1;
    --cover-white: #f7f7f8;
    --navy: #0f3a86;
    --navy-deep: #0a2a6b;
    --navy-light: #2f5aa8;
    --title-blue: #0d47a1;
    --accent-orange: #f5a52a;
    --author-blue: #2a56a6;
    --illo-blue: #3f7fd6;
    --illo-blue-dark: #1f4fa8;
    --illo-peach: #f8c889;
  }
  * { box-sizing: border-box; margin: 0; padding: 0; }
  html, body {
    width: 1200px;
    height: 900px;
    overflow: hidden;
    background: var(--page-bg);
    font-family: "Montserrat", Arial, sans-serif;
  }
  .book-cover {
    position: absolute;
    left: 300px;
    top: 26px;
    width: 600px;
    height: 848px;
    background: linear-gradient(180deg, #ffffff 0%, var(--cover-white) 60%, #ececee 100%);
    overflow: hidden;
    box-shadow: 0 10px 30px rgba(0,0,0,0.18);
  }
  .spine-band {
    position: absolute;
    top: 0;
    right: 0;
    width: 168px;
    height: 100%;
    background: linear-gradient(170deg, var(--navy-deep) 0%, var(--navy) 45%, var(--navy-light) 60%, var(--navy-deep) 100%);
  }
  .cover-title {
    position: absolute;
    left: 110px;
    top: 300px;
    width: 300px;
  }
  .cover-title__main {
    font-weight: 800;
    font-size: 38px;
    line-height: 1.05;
    color: var(--title-blue);
    letter-spacing: -0.3px;
  }
  .cover-title__sub {
    margin-top: 4px;
    font-weight: 300;
    font-size: 27px;
    line-height: 1.12;
    color: var(--accent-orange);
    text-transform: uppercase;
  }
  .cover-title__rule {
    margin-top: 12px;
    width: 60px;
    height: 4px;
    background: var(--title-blue);
  }
  .cover-illustration {
    position: absolute;
    left: 318px;
    top: 500px;
    width: 236px;
    height: 240px;
    border-radius: 6px;
    background: linear-gradient(160deg, var(--illo-blue) 0%, var(--illo-peach) 45%, var(--illo-blue) 70%, var(--illo-blue-dark) 100%);
  }
  .cover-author {
    position: absolute;
    left: 150px;
    bottom: 58px;
    font-weight: 400;
    font-size: 30px;
    color: var(--author-blue);
    letter-spacing: 0.4px;
  }
</style>
</head>
<body>
  <main class="book-cover">
    <div class="spine-band"></div>
    <header class="cover-title">
      <h1 class="cover-title__main">The corner<br>shop</h1>
      <p class="cover-title__sub">Keeper's<br>Handbook</p>
      <div class="cover-title__rule"></div>
    </header>
    <div class="cover-illustration" role="img" aria-label="Isometric illustration of a small two-storey shop with a striped awning on a blue base, surrounded by floating money, location and chart icons"></div>
    <p class="cover-author">Author Name</p>
  </main>
</body>
</html>
```